Real Estate Business card design

Company Name: Tamarind Holdings, LLC
subtitle: We pay cash for houses!
Daniel Whitcombe
Managing Director
555-214-0963
Dan@TamarindHoldingsLLC.example
www.TamarindHoldingsLLC.example

We pay referral fees for Seller and Buyer leads.

Back:
We offer referral fees for Seller and Buyer leads that close.

Please contact Hal at 555-214-0963 with your referrals or to learn more about the referral program!

I am open to different color options but I am going for a classic, elegant, clean, and professional look. Please use logo as a reference.

Target Market(s)

People selling their homes and people in the market for buying homes.

Contact Information for Business Card

please see project description

Font styles to use
Serif
Sans Serif
Script

Requirements
Must have
• must have my logo in it
Nice to have
• I like cards that are split down the middle but please come up with a few mock ups. Open to any color scheme.

```html
<!DOCTYPE html>
<html lang="en">
<head>
<meta charset="utf-8">
<title>Tamarind Holdings, LLC – Business Card</title>
<link href="https://fonts.googleapis.com/css2?family=Lato:wght@400;700;900&family=Montserrat:wght@600;700&display=swap" rel="stylesheet">
<style>
  :root {
    --backdrop: #7a8082;
    --card-dark: #141414;
    --card-light: #f4f3ef;
    --gold: #c29a6c;
    --navy: #2f3a4a;
    --ink: #1b1f26;
    --silver: #9a9a9a;
  }
  * { box-sizing: border-box; margin: 0; padding: 0; }
  html, body { width: 1200px; height: 959px; overflow: hidden; }
  body {
    background: var(--backdrop);
    font-family: "Lato", sans-serif;
    position: relative;
  }
  .card {
    position: absolute;
    width: 580px;
    height: 332px;
    border-radius: 26px;
    box-shadow: 0 14px 30px rgba(0,0,0,.35);
    overflow: hidden;
  }
  .card--back { left: 80px; top: 90px; background: var(--card-dark); }
  .card--front { left: 540px; top: 530px; background: var(--card-light); }

  .brand {
    position: absolute;
    display: flex;
    align-items: center;
    gap: 12px;
    font-family: "Lato", sans-serif;
    font-weight: 700;
    line-height: 1.1;
  }
  .brand__square { width: 18px; height: 18px; background: var(--gold); flex: none; }
  .card--back .brand { left: 0; right: 0; top: 120px; justify-content: center; font-size: 34px; color: var(--silver); }
  .card--front .brand { left: 40px; top: 118px; width: 220px; font-size: 26px; color: var(--navy); }

  .back-tagline {
    position: absolute;
    left: 0; right: 0; bottom: 36px;
    text-align: center;
    font-family: "Montserrat", sans-serif;
    font-weight: 600;
    font-size: 14px;
    letter-spacing: .4px;
    color: var(--gold);
  }

  .details { position: absolute; left: 300px; top: 44px; width: 260px; color: var(--ink); }
  .details__company { font-weight: 900; font-size: 20px; color: var(--navy); line-height: 1.1; }
  .details__slogan { font-size: 15px; color: var(--navy); margin-top: 2px; }
  .details__name { font-weight: 900; font-size: 19px; margin-top: 22px; }
  .contact { list-style: none; margin-top: 8px; }
  .contact li { display: flex; align-items: center; gap: 8px; font-size: 12px; margin-bottom: 7px; white-space: nowrap; }
  .contact svg { width: 12px; height: 12px; flex: none; }

  .front-tagline {
    position: absolute;
    left: 0; right: 0; bottom: 34px;
    text-align: center;
    font-family: "Montserrat", sans-serif;
    font-weight: 700;
    font-size: 14px;
    letter-spacing: .3px;
    color: var(--ink);
  }
</style>
</head>
<body>
  <section class="card card--back" aria-label="Card back">
    <div class="brand"><span class="brand__square"></span>Tamarind Holdings, LLC</div>
    <p class="back-tagline">WE OFFER REFERRAL FEES FOR SELLER AND BUYER LEADS THAT CLOSE</p>
  </section>

  <section class="card card--front" aria-label="Card front">
    <div class="brand"><span class="brand__square"></span><span>Tamarind<br>Holdings, LLC</span></div>
    <div class="details">
      <p class="details__company">Tamarind Holdings, LLC</p>
      <p class="details__slogan">We pay cash for houses!</p>
      <p class="details__name">Daniel Whitcombe</p>
      <ul class="contact">
        <li>
          <svg viewBox="0 0 24 24" aria-hidden="true"><path fill="#c29a6c" d="M6.6 10.8a15 15 0 0 0 6.6 6.6l2.2-2.2a1 1 0 0 1 1-.25 11.4 11.4 0 0 0 3.6.57 1 1 0 0 1 1 1V20a1 1 0 0 1-1 1A17 17 0 0 1 3 4a1 1 0 0 1 1-1h3.5a1 1 0 0 1 1 1c0 1.25.2 2.45.57 3.6a1 1 0 0 1-.25 1z"/></svg>
          555-214-0963
        </li>
        <li>
          <svg viewBox="0 0 24 24" aria-hidden="true"><path fill="#c29a6c" d="M2 5h20v14H2z"/><path fill="none" stroke="#f4f3ef" stroke-width="1.6" d="M2 5l10 8 10-8"/></svg>
          Dan@TamarindHoldingsLLC.example
        </li>
        <li>
          <svg viewBox="0 0 24 24" aria-hidden="true"><g fill="none" stroke="#c29a6c" stroke-width="1.8"><circle cx="12" cy="12" r="9"/><ellipse cx="12" cy="12" rx="4" ry="9"/><path d="M3 12h18"/></g></svg>
          www.TamarindHoldingsLLC.example
        </li>
      </ul>
    </div>
    <p class="front-tagline">WE PAY REFERRAL FEES FOR SELLER AND BUYER LEADS</p>
  </section>
</body>
</html>
```